Coaching landingpage/salespage need a layout

Hi!
We are two people from Sweden looking for help to design our coaching landingpage/salespage.

What about:
We need a nice modern timeless appealing Photoshop layout (landingpage) for our coaching page where we coach people to “how to get a richer lifestyle”.

Style of page:
We want the site to reflect seriousness but still harmonic. We would like somewhat colorful and (but not too crazy). After all, we are coaching about investments and private economy.
Responsive layout – consider stacking order when scaling down window width. Fullpage-design where content areas are 960 grid/max-width.

----------------------------------------------------------------------------
Content on page:
*Headersection – Logo and header image with the two coaches together and space for later on adding a video.

*On the landingpage the customers can read up on what we mean by a richer lifestyle (use dummy text). We show our Trivselsnyckeln (= Lifestyle matrix) and a little description about that. If the customers want to know more, they can click "read more (or a symbolic icon that relates to read more)" to expand a hidden div (section) where they can read more about Trivselsnyckeln. They can also minimize the section.

*3-4 Unique selling points “Four reasons why choose coaching” with nice designed number-icons and some place for text.

*The customer should also be able to read something about what happens during a typical coaching session, some bullets that summarize it (use dummy text) and a couple of headlines, maybe 3 or 4 (about what they need to prepare for themselves .eg Skype, headset/microphone etc).

*Offer/product section: A section where the customer can see what services we provide, choose product and click order. When customer click order they will arrive to an order-page (this one you don’t have to design) .
Our products are as followed: Bronze (single coaching session), Silver (small-package), Gold (large-package). Use provided graphics for these products.

*Testimonials section. Currently we have 2 good testimonials, but only with text no portrait picture.

Testimonial1: “Uppiggande och inspirerande! Kommer med enkla vardagstips såväl som svårare tips. Ett roligt sätt att få en spark i baken, så att ekonomi-energin bibehålls! Tack för ett bra samtal!" - Josefin Brandeby

Testimonial2: "Värdefullast för mig var kunskapen om alternativa investeringssställen som inte är börs eller eget ägande." - Annika Sjöhalla

*Section with portraits and info about the coaches (currently 2 coaches, but in future will be several, so a design-section that’s lets us add more coaches).

*Footer-section
------------------------------------------------------------------------

Colors:
Use Trivselsnyckeln (attached file) as colorinspiration. Doesn’t have to be exactly those colors, you can use similar colors if it is more pleasing to the eye and you can also use complementary colors.

Currently we have tried of our own but don't really nail it with any apealing design. This is what we have done so far but we want to replace it with your more professional design:

https://www.harbekrona.se/full/Page/coaching13
-------------------------------------------------------------

SUMMARIZE of the above design-description:

* Our logo (attached psd-file with smart-object. You can try different colors with color-overlay)

*Apealing headerimage with portrait (attached file "big_portrait")

*Introduction text (use dummy text about 100 words)

*Text about Trivselsnyckeln (use dummy text about 200 words)

*Trivselsnyckeln (attached psd-file with smart-object)

*What we are covering during a coaching session (dummy text about 200 words and about 5 or 6 bullets)

*3-4 Unique Selling Points with stylish number icons (not 2 small) and some text.
*Our offers Bronze, Silver, Gold (attached pictures)
*Testimonials
*Picture & info about coaches (attached pictures, choose whichever suits you)
*Footer

Please comment if there are questions.

Reagards Torbjörn @ Harbe Krona

Target Market(s)

People who want to learn how to create a richer lifestyle which involves more freedom and a better well-being

Number of Pages Required

1 page

Font styles to use
Sans Serif
Other font styles liked:
• Roboto

Requirements
Should not have
• A cheezy unmodern landingpage with lots of texts and 10 sign-up buttons.
• This page is not a site about capturing emails and building lists by provide a "best-guide-for-something". It´s about getting people to book and pay for one or more coaching-sessions.

```html
<!DOCTYPE html>
<html lang="sv">
<head>
<meta charset="utf-8">
<title>Harbe Krona – Coaching</title>
<link href="https://fonts.googleapis.com/css2?family=Cabin:wght@400;500;600&family=Open+Sans:wght@400;600;700&display=swap" rel="stylesheet">
<style>
:root{
  --brand:#2d8fc4;
  --ink:#2b2b2b;
  --muted:#666;
  --tint:#d3e2ec;
  --card:#ececec;
  --green:#3aa655;
  --orange:#f19a2c;
  --brown:#8a4b1a;
  --dark:#2a2a2a;
  --darker:#1f1f1f;
  --white:#fff;
}
*{margin:0;padding:0;box-sizing:border-box}
html,body{width:1200px;height:4737px;overflow:hidden}
body{font-family:"Open Sans",Arial,sans-serif;color:var(--ink);background:var(--white);position:relative}
h2,h3,h4{font-family:"Cabin",Arial,sans-serif;font-weight:500}
.section{position:absolute;left:0;width:1200px}
.section-title{text-align:center;font-size:36px;color:var(--ink)}
.lead{font-size:13.5px;line-height:1.75;color:#555;text-align:center}
/* hero */
.hero{top:0;height:575px;background:linear-gradient(180deg,#cfa25a 0%,#b98a44 35%,#6b4d2b 70%,#3d2b1a 100%)}
.brand{position:absolute;top:38px;left:0;width:1200px;display:flex;justify-content:center;align-items:center;gap:12px}
.brand-mark{width:30px;height:30px;background:var(--brand)}
.brand-name{font-family:"Cabin",Arial,sans-serif;font-size:28px;font-weight:500;color:var(--brand);letter-spacing:2px;text-transform:uppercase}
.coaches-photo{position:absolute;left:95px;top:250px;width:520px;height:325px;background:linear-gradient(180deg,#9aa3ad,#3a3f47)}
.video-frame{position:absolute;left:606px;top:237px;width:436px;height:284px;border:6px solid var(--white);background:linear-gradient(135deg,#c9cdd2,#7d868f)}
.play{position:absolute;left:182px;top:106px}
/* intro */
.intro{top:575px;height:303px}
.intro .section-title{margin-top:65px}
.intro .lead{width:860px;margin:22px auto 0}
/* matrix */
.matrix{top:878px;height:625px;background:var(--tint)}
.matrix-art{position:absolute;left:158px;top:62px;width:492px;height:492px;border-radius:50%;background:radial-gradient(circle at 50% 45%,#4a9ad6 0%,#2f82c4 70%,#2a74b0 100%)}
.matrix-text{position:absolute;left:682px;top:105px;width:355px}
.matrix-text h2{font-size:34px;margin-bottom:14px}
.matrix-text p{font-size:13.5px;line-height:1.72;color:#555}
.btn-outline{display:inline-flex;align-items:center;gap:10px;margin-top:30px;border:2px solid var(--brand);color:var(--brand);font-size:12px;font-weight:700;padding:8px 18px;text-transform:uppercase}
/* reasons */
.reasons{top:1503px;height:584px}
.reasons .section-title{margin-top:72px}
.reason{position:absolute;top:202px;width:206px;height:307px;background:var(--card);text-align:center;padding:96px 18px 0}
.reason-icon{position:absolute;left:53px;top:-52px;width:100px;height:100px;border-radius:50%;background:var(--white);box-shadow:0 2px 6px rgba(0,0,0,.15);display:flex;align-items:center;justify-content:center}
.reason h3{font-size:21px;margin-bottom:10px}
.reason p{font-size:12.5px;line-height:1.65;color:#666}
/* session */
.session{top:2087px;height:708px;background:linear-gradient(90deg,#2a3442 0%,#3e4a5c 40%,#8a7e78 70%,#b9a9a0 100%)}
.session-box{position:absolute;left:663px;top:76px;width:316px;height:553px;background:var(--white);padding:28px 22px}
.session-box h2{font-size:32px;line-height:1.08;margin-bottom:20px}
.session-box h4{font-family:"Open Sans",Arial,sans-serif;font-size:13px;font-weight:700;line-height:1.4;margin:18px 0 6px}
.session-box ul{list-style:none}
.session-box li{font-size:12.5px;line-height:1.75;color:#555}
.session-box li::before{content:"•";margin-right:6px}
/* products */
.products{top:2795px;height:647px}
.products .section-title{margin-top:72px}
.products .sub{text-align:center;font-size:15px;color:#666;margin-top:8px}
.product{position:absolute;top:189px;width:253px;height:379px;background:var(--card);text-align:center}
.medal{margin:55px auto 0;width:140px;height:140px;border-radius:50%}
.bronze{background:radial-gradient(circle at 35% 30%,#f2b27a,#c8702d 60%,#8e4a18)}
.silver{background:radial-gradient(circle at 35% 30%,#ffffff,#bdbdbd 60%,#868686)}
.gold{background:radial-gradient(circle at 35% 30%,#fff0a0,#e5bb2a 60%,#a67c0a)}
.product h3{font-size:20px;margin-top:22px;text-transform:uppercase;font-weight:600}
.product p{font-size:14px;color:#555;line-height:1.5;margin-top:4px}
.btn-order{display:inline-block;margin-top:22px;background:var(--green);color:var(--white);font-size:13px;font-weight:700;padding:9px 26px;text-transform:uppercase;border-bottom:3px solid #2c8243}
/* testimonials */
.testimonials{top:3442px;height:442px;background:var(--orange)}
.testimonials .section-title{margin-top:68px;color:var(--ink)}
.quote{position:absolute;top:174px;height:205px;background:var(--white);border-radius:6px;text-align:center;padding:48px 38px 0}
.quote-mark{position:absolute;left:50%;top:-24px;margin-left:-24px;width:48px;height:48px;border-radius:50%;background:var(--brown);color:var(--white);font-family:Georgia,serif;font-size:40px;line-height:58px;font-weight:700}
.quote p{font-style:italic;font-size:14px;line-height:1.65;color:#444}
.quote cite{display:block;margin-top:14px;font-style:normal;font-weight:700;font-size:15px}
/* coaches */
.coaches{top:3884px;height:395px}
.coaches .section-title{margin-top:68px}
.coach{position:absolute;top:149px;height:208px;background:var(--white);border:1px solid #ddd;display:flex}
.coach-photo{width:205px;height:100%;background:linear-gradient(180deg,#8d8f94,#3c4048)}
.coach-info{padding:20px 18px;flex:1}
.coach-info h3{font-family:"Open Sans",Arial,sans-serif;font-size:17px;font-weight:700}
.coach-info a{font-size:12.5px;color:var(--brand);text-decoration:none}
.coach-info p{font-size:12.5px;line-height:1.6;color:#666;margin-top:14px}
/* connect */
.connect{top:4279px;height:143px;text-align:center}
.connect h4{font-family:"Open Sans",Arial,sans-serif;font-weight:400;font-size:19px;color:#8a8a8a;letter-spacing:1px;margin-top:30px;text-transform:uppercase}
.social{position:absolute;left:0;width:1200px;top:88px;display:flex;justify-content:center;gap:8px}
.social span{width:55px;height:55px;background:var(--brand)}
/* footer */
.footer{top:4422px;height:315px;background:var(--dark);color:#ddd}
.footer-nav{display:flex;justify-content:center;gap:38px;margin-top:32px;font-size:12px;text-transform:uppercase}
.footer-brand{position:absolute;top:78px;left:0;width:1200px;display:flex;justify-content:center;align-items:center;gap:10px}
.footer-brand .brand-mark{width:24px;height:24px}
.footer-brand .brand-name{font-size:22px}
.newsletter{position:absolute;top:145px;left:240px;width:720px;display:flex;align-items:center;gap:14px;border-top:1px solid #444;padding-top:14px}
.newsletter label{font-weight:700;font-size:16px;text-transform:uppercase;color:var(--white)}
.newsletter .field{width:310px;height:30px;background:var(--white);font-size:12px;color:#999;padding:7px 10px}
.newsletter .btn{background:var(--brand);color:var(--white);font-size:12px;font-weight:700;padding:8px 14px;text-transform:uppercase}
.contact{position:absolute;top:208px;left:220px;width:760px;display:flex;justify-content:space-between;font-size:12px;border-top:1px solid #444;border-bottom:1px solid #444;padding:12px 0}
.contact span{display:flex;align-items:center;gap:8px}
.copyright{position:absolute;bottom:0;left:0;width:1200px;height:50px;background:var(--darker);text-align:center;font-size:12px;color:#aaa;line-height:50px}
</style>
</head>
<body>

<header class="section hero" role="img" aria-label="Wheat field at sunset with a young plant growing from a wooden table">
  <div class="brand"><span class="brand-mark"></span><span class="brand-name">Harbe Krona</span></div>
  <div class="coaches-photo" role="img" aria-label="Portrait of the two coaches standing together"></div>
  <div class="video-frame" role="img" aria-label="Video still of a coaching meeting around a table">
    <svg class="play" width="60" height="60" viewBox="0 0 60 60"><circle cx="30" cy="30" r="28" fill="#fff"/><path d="M24 18 L42 30 L24 42 Z" fill="#222"/></svg>
  </div>
</header>

<section class="section intro">
  <h2 class="section-title">What We Mean By a Richer Lifestyle</h2>
  <p class="lead">Lorem ipsum dolor sit amet, consectetur adipisicing elit, sed do eiusmod tempor incididunt ut labore et dolore magna aliqua. Ut enim ad minim veniam, quis nostrud exercitation ullamco laboris nisi ut aliquip ex ea commodo consequat. Duis aute irure dolor in reprehenderit in voluptate velit esse cillum dolore eu fugiat nulla pariatur. Excepteur sint occaecat cupidatat non proident, sunt in culpa qui officia deserunt mollit anim id est laborum.</p>
</section>

<section class="section matrix">
  <div class="matrix-art" role="img" aria-label="Trivselsnyckeln lifestyle matrix illustration"></div>
  <div class="matrix-text">
    <h2>Our Trivselsnyckeln</h2>
    <p>Lorem ipsum dolor sit amet, consectetur adipisicing elit, sed do eiusmod tempor incididunt ut labore et dolore magna aliqua. Ut enim ad minim veniam, quis nostrud exercitation ullamco laboris nisi ut aliquip ex ea commodo consequat. Duis aute irure dolor in reprehenderit in voluptate velit esse cillum dolore eu fugiat nulla pariatur. Excepteur sint occaecat cupidatat non proident, sunt in culpa qui officia deserunt mollit anim id est laborum.</p>
    <span class="btn-outline">Read more
      <svg width="16" height="16" viewBox="0 0 16 16"><circle cx="8" cy="8" r="7" fill="none" stroke="currentColor" stroke-width="1.6"/><path d="M8 4v8M4 8h8" stroke="currentColor" stroke-width="1.6"/></svg>
    </span>
  </div>
</section>

<section class="section reasons">
  <h2 class="section-title">Why Choose Coaching</h2>
  <div class="reason" style="left:164px">
    <div class="reason-icon"><svg width="50" height="50" viewBox="0 0 50 50"><circle cx="25" cy="25" r="22" fill="#e23b2e"/><circle cx="25" cy="25" r="15" fill="#fff"/><circle cx="25" cy="25" r="8" fill="#e23b2e"/><path d="M25 25 L44 6" stroke="#333" stroke-width="2.5"/></svg></div>
    <h3>Targeting</h3>
    <p>Lorem ipsum dolor sit amet, consectetur adipisicing elit, sed do eiusmod tempor incididunt ut labore et dolore magna aliqua. Ut enim ad minim veniam.</p>
  </div>
  <div class="reason" style="left:385px">
    <div class="reason-icon"><svg width="50" height="50" viewBox="0 0 50 50"><circle cx="25" cy="25" r="18" fill="none" stroke="#f0a500" stroke-width="6" stroke-dasharray="6 4"/><circle cx="25" cy="25" r="11" fill="#f0a500"/><path d="M25 17v16M21 21h6a2 2 0 0 1 0 4h-4a2 2 0 0 0 0 4h6" stroke="#fff" stroke-width="2" fill="none"/></svg></div>
    <h3>Creating</h3>
    <p>Lorem ipsum dolor sit amet, consectetur adipisicing elit, sed do eiusmod tempor incididunt ut labore et dolore magna aliqua. Ut enim ad minim veniam.</p>
  </div>
  <div class="reason" style="left:606px">
    <div class="reason-icon"><svg width="50" height="50" viewBox="0 0 50 50"><path d="M8 8 L42 42 M42 8 L8 42" stroke="#3b6fb6" stroke-width="3"/><circle cx="8" cy="8" r="5" fill="#e23b2e"/><circle cx="42" cy="8" r="5" fill="#3aa655"/><circle cx="8" cy="42" r="5" fill="#f0a500"/><circle cx="42" cy="42" r="5" fill="#8e44ad"/></svg></div>
    <h3>Shaping</h3>
    <p>Lorem ipsum dolor sit amet, consectetur adipisicing elit, sed do eiusmod tempor incididunt ut labore et dolore magna aliqua. Ut enim ad minim veniam.</p>
  </div>
  <div class="reason" style="left:827px">
    <div class="reason-icon"><svg width="50" height="50" viewBox="0 0 50 50"><circle cx="25" cy="25" r="20" fill="#1f3d6b"/><circle cx="25" cy="20" r="8" fill="#f0a500"/></svg></div>
    <h3>Capturing</h3>
    <p>Lorem ipsum dolor sit amet, consectetur adipisicing elit, sed do eiusmod tempor incididunt ut labore et dolore magna aliqua. Ut enim ad minim veniam.</p>
  </div>
</section>

<section class="section session" role="img" aria-label="Speaker in a suit addressing a seated audience at a seminar">
  <div class="session-box">
    <h2>What Happens During a Typical Coaching Session</h2>
    <h4>Lorem ipsum dolor sit amet, consectetur adipiscing elit</h4>
    <ul><li>Lorem ipsum dolor sit amet.</li><li>Consectetur adipiscing elit.</li><li>Integer vel est nec metus lobortis.</li></ul>
    <h4>Lorem ipsum dolor sit amet, consectetur adipiscing elit</h4>
    <ul><li>Lorem ipsum dolor sit amet.</li><li>Consectetur adipiscing elit.</li><li>Integer vel est nec metus lobortis.</li></ul>
    <h4>Lorem ipsum dolor sit amet, consectetur adipiscing elit</h4>
    <ul><li>Lorem ipsum dolor sit amet.</li><li>Consectetur adipiscing elit.</li><li>Integer vel est nec metus lobortis.</li></ul>
  </div>
</section>

<section class="section products">
  <h2 class="section-title">Our Products</h2>
  <p class="sub">Choose product and click order</p>
  <div class="product" style="left:167px">
    <div class="medal bronze" role="img" aria-label="Bronze medal"></div>
    <h3>Bronze</h3><p>Single coaching session<br>Pris 650 SEK</p>
    <span class="btn-order">Order now</span>
  </div>
  <div class="product" style="left:470px">
    <div class="medal silver" role="img" aria-label="Silver medal"></div>
    <h3>Silver</h3><p>Small package<br>&nbsp;</p>
    <span class="btn-order">Order now</span>
  </div>
  <div class="product" style="left:777px">
    <div class="medal gold" role="img" aria-label="Gold medal"></div>
    <h3>Gold</h3><p>Large package<br>Pris 5800 SEK</p>
    <span class="btn-order">Order now</span>
  </div>
</section>

<section class="section testimonials">
  <h2 class="section-title">Testimonials</h2>
  <blockquote class="quote" style="left:174px;width:401px">
    <span class="quote-mark">“</span>
    <p>"Uppiggande och inspirerande! Kommer med enkla vardagstips såväl som svårare tips. Ett roligt sätt att få en spark i baken, så att ekonomi-energin bibehålls! Tack för ett bra samtal!"</p>
    <cite>- Josefin Brandeby</cite>
  </blockquote>
  <blockquote class="quote" style="left:610px;width:423px">
    <span class="quote-mark">“</span>
    <p>"Värdefullast för mig var kunskapen om alternativa investeringsställen som inte är börs eller eget ägande."</p>
    <cite>- Annika Sjöhalla</cite>
  </blockquote>
</section>

<section class="section coaches">
  <h2 class="section-title">About The Coaches</h2>
  <article class="coach" style="left:167px;width:411px">
    <div class="coach-photo" role="img" aria-label="Portrait of coach Torbjörn Wallgren"></div>
    <div class="coach-info"><h3>Torbjörn Wallgren</h3><a>torbjorn@harbekrona.se</a>
      <p>Sed ut perspiciatis unde omnis iste natus error sit voluptatem accusantium doloremque laudantium, totam rem aperiam.</p></div>
  </article>
  <article class="coach" style="left:610px;width:423px">
    <div class="coach-photo" role="img" aria-label="Portrait of coach Henrik Ståldal"></div>
    <div class="coach-info"><h3>Henrik Ståldal</h3><a>henrik@harbekrona.se</a>
      <p>Sed ut perspiciatis unde omnis iste natus error sit voluptatem accusantium doloremque laudantium, totam rem aperiam.</p></div>
  </article>
</section>

<section class="section connect">
  <h4>Connect with Harbe Krona</h4>
  <div class="social"><span></span><span></span><span></span><span></span></div>
</section>

<footer class="section footer">
  <nav class="footer-nav"><span>Home</span><span>About us</span><span>Blog</span><span>Coaching</span><span>Testimonials</span><span>Contact us</span></nav>
  <div class="footer-brand"><span class="brand-mark"></span><span class="brand-name">Harbe Krona</span></div>
  <div class="newsletter"><label>Sign up for our newsletter</label><span class="field">Enter your email address</span><span class="btn">Subscribe</span></div>
  <div class="contact">
    <span><svg width="14" height="18" viewBox="0 0 14 18"><path d="M7 0a7 7 0 0 1 7 7c0 5-7 11-7 11S0 12 0 7a7 7 0 0 1 7-7z" fill="#ddd"/><circle cx="7" cy="7" r="2.5" fill="#2a2a2a"/></svg>Harbe Krona AB, Lindvägen 12, 41260 Göteborg</span>
    <span><svg width="16" height="16" viewBox="0 0 16 16"><path d="M3 1l3 3-2 2c1 2 3 4 5 5l2-2 3 3-2 3C7 15 1 9 0 3z" fill="#ddd"/></svg>(0)31 40 22 180</span>
    <span><svg width="18" height="13" viewBox="0 0 18 13"><rect width="18" height="13" fill="#ddd"/><path d="M0 0l9 7 9-7" stroke="#2a2a2a" stroke-width="1.5" fill="none"/></svg>team@harbekrona.se</span>
  </div>
  <div class="copyright">©2016 Harbe Krona AB . All Rights Reserved</div>
</footer>

</body>
</html>
```